Create a sign for my school of biodynamic craniosacral therapy: Lumen Harbor

Hello, I would like to get a designer to make me a sign. I have a logo in mind. The sign will be about 7' X 3' or 4' big. ( in feet)
I have another site to transfer the design to make the sign with.
I attached a few logos I like. I need the sign to be easy to read for cars driving by, without too much information. I would like it to look original and holistic. Also have a whimsical and sky and earth quality.
my website will give you a feel www.lumenharbor.example
The last picture of the "Tarn Goods" sign is a sample of how I will make the entire sign structure.

Target Market(s)

body worker students

Industry/Entity Type

School and healthcare

Font styles to use
Decorative
Other font styles liked:
• dead hardy, milonga, ribeye,sketch block , train one

Colors

Designer to choose colors to be used in the design.

Requirements
Must have
• easy to read, highly visible, organic looking
Nice to have
• simular to my design
Should not have
• look too commercial

```html
<!DOCTYPE html>
<html lang="en">
<head>
<meta charset="utf-8">
<title>Lumen Harbor — Roadside Sign</title>
<link href="https://fonts.googleapis.com/css2?family=Open+Sans:wght@400&family=Poppins:wght@600;700&display=swap" rel="stylesheet">
<style>
  :root {
    --page: #ffffff;
    --slate: #4f6676;
    --slate-weathered: #7f9aab;
    --post-core: #08120f;
    --ink: #1c1715;
    --black: #000000;
    --white: #ffffff;
    --bracket: #9a8f72;
    --bracket-light: #c9bea4;
    --wood: #d8cfbf;
    --wood-ink: #3b3631;
    --frame-walnut: #4a4038;
    --frame-ocean: #123b57;
    --frame-moss: #1f6e2c;
    --frame-wine: #4b1c1f;
    --phone-cream: #ece2d0;
    --rule-grey: #bdbdbd;
    --dim-ink: #222222;
  }
  * { box-sizing: border-box; margin: 0; padding: 0; }
  html, body { width: 1200px; height: 1160px; overflow: hidden; background: var(--page); }
  body { position: relative; font-family: "Poppins", sans-serif; color: var(--ink); }

  /* dimension callouts */
  .dim-tick { position: absolute; background: var(--dim-ink); }
  .dim-line { position: absolute; background: var(--rule-grey); }
  .dim-label { position: absolute; font-family: "Open Sans", sans-serif; font-size: 15px; color: var(--dim-ink); white-space: nowrap; transform: translate(-50%, -50%); }

  /* sign structure */
  .sign { position: absolute; width: 407px; height: 933px; }
  .sign--plan { left: 83px; top: 135px; }
  .sign--finish { left: 710px; top: 130px; }

  .header-band { position: absolute; left: 0; top: 0; width: 407px; height: 350px; background: var(--slate); }
  .post { position: absolute; top: 350px; bottom: 0; }
  .post--outer-left { left: 0; width: 36px; background: var(--slate); }
  .post--core-left { left: 36px; width: 11px; background: var(--post-core); }
  .post--core-right { left: 360px; width: 11px; background: var(--post-core); }
  .post--outer-right { left: 371px; width: 36px; background: var(--slate); }

  .header-board { position: absolute; left: 22px; top: 23px; width: 364px; height: 298px; background: var(--white); }
  .header-frame { position: absolute; left: 28px; top: 30px; width: 349px; height: 285px; border: 4px solid var(--ink); }

  .practitioner { position: absolute; left: 0; width: 407px; top: 37px; text-align: center; font-size: 15px; font-weight: 700; letter-spacing: 0.02em; }
  .ornament { position: absolute; left: 162px; top: 73px; width: 86px; height: 30px; border-radius: 15px; background: #e6e3e1; }
  .school-name { position: absolute; left: 0; width: 407px; top: 110px; text-align: center; font-size: 33px; line-height: 29px; font-weight: 700; letter-spacing: 0.17em; padding-left: 0.17em; }
  .emblem { position: absolute; left: 113px; top: 176px; width: 187px; height: 96px; background: #e9e7e5; }
  .header-rule { position: absolute; left: 56px; top: 283px; width: 299px; height: 2px; background: var(--ink); }
  .tagline { position: absolute; left: 0; width: 407px; top: 287px; text-align: center; font-size: 9.5px; font-weight: 600; letter-spacing: 0.13em; }

  .plate { position: absolute; left: 58px; width: 292px; height: 92px; border: 2px solid var(--ink); background: var(--white); }
  .plate--1 { top: 381px; }
  .plate--2 { top: 488px; }
  .plate--3 { top: 592px; }
  .plate--4 { top: 699px; }
  .plate-face { position: absolute; left: 18px; top: 8px; width: 252px; height: 73px; border: 2.5px solid var(--black); display: flex; align-items: center; justify-content: center; text-align: center; font-weight: 700; color: var(--black); letter-spacing: -0.01em; }
  .plate-face--name { font-size: 31px; line-height: 30px; padding-top: 3px; }
  .plate-face--service { font-size: 26px; }
  .plate-face--service-lg { font-size: 31px; }
  .plate-face--phone { background: var(--black); color: var(--white); font-size: 38px; font-weight: 600; letter-spacing: -0.04em; }

  .bracket { position: absolute; width: 27px; height: 14px; background: var(--bracket); }
  .bracket--left { left: 43px; }
  .bracket--right { left: 337px; }
  .bracket::after { content: ""; position: absolute; top: 6px; width: 2px; height: 2px; background: var(--post-core); }
  .bracket--left::after { right: 4px; }
  .bracket--right::after { left: 4px; }
  .bracket--r1 { top: 420px; }
  .bracket--r2 { top: 527px; }
  .bracket--r3 { top: 631px; }
  .bracket--r4 { top: 738px; }

  /* finished colourway */
  .sign--finish .header-band,
  .sign--finish .post--outer-left,
  .sign--finish .post--outer-right { background: var(--slate-weathered); }
  .sign--finish .header-board { background: var(--wood); box-shadow: 0 2px 4px rgba(0,0,0,0.25); }
  .sign--finish .header-frame { border-color: var(--wood-ink); border-width: 3px; }
  .sign--finish .practitioner,
  .sign--finish .school-name,
  .sign--finish .tagline { color: var(--wood-ink); }
  .sign--finish .header-rule { background: var(--wood-ink); }
  .sign--finish .ornament { background: #c9bfae; }
  .sign--finish .emblem { background: #cdc3b2; }
  .sign--finish .plate { border: none; box-shadow: 0 2px 4px rgba(0,0,0,0.3); }
  .sign--finish .plate--1 { background: var(--frame-walnut); }
  .sign--finish .plate--2 { background: var(--frame-ocean); }
  .sign--finish .plate--3 { background: var(--frame-moss); }
  .sign--finish .plate--4 { background: var(--wood); }
  .sign--finish .plate-face { border: 2px solid #f4eee3; background: var(--wood); color: var(--wood-ink); }
  .sign--finish .plate-face--phone { left: 14px; width: 264px; border: none; background: var(--frame-wine); color: var(--phone-cream); }
  .sign--finish .bracket { background: var(--bracket-light); }
</style>
</head>
<body>

  <!-- width callout -->
  <div class="dim-tick" style="left:83px; top:76px; width:1px; height:44px;"></div>
  <div class="dim-tick" style="left:490px; top:76px; width:1px; height:44px;"></div>
  <div class="dim-line" style="left:94px; top:98px; width:150px; height:1px;"></div>
  <div class="dim-line" style="left:329px; top:98px; width:150px; height:1px;"></div>
  <div class="dim-label" style="left:290px; top:96px;">36" wide</div>

  <!-- height callout -->
  <div class="dim-tick" style="left:499px; top:134px; width:44px; height:1px;"></div>
  <div class="dim-tick" style="left:499px; top:1068px; width:44px; height:1px;"></div>
  <div class="dim-line" style="left:521px; top:148px; width:1px; height:418px;"></div>
  <div class="dim-line" style="left:521px; top:643px; width:1px; height:418px;"></div>
  <div class="dim-label" style="left:533px; top:603px;">82" tall</div>

  <!-- line plan -->
  <section class="sign sign--plan" aria-label="Sign layout, line plan">
    <div class="header-band"></div>
    <div class="post post--outer-left"></div>
    <div class="post post--core-left"></div>
    <div class="post post--core-right"></div>
    <div class="post post--outer-right"></div>
    <div class="header-board"></div>
    <div class="header-frame"></div>
    <p class="practitioner">DR. MARA VELDEN, DC, BCST</p>
    <div class="ornament" role="img" aria-label="Small knotwork ornament"></div>
    <h1 class="school-name">LUMEN<br>HARBOR</h1>
    <div class="emblem" role="img" aria-label="Area for the school emblem artwork"></div>
    <div class="header-rule"></div>
    <p class="tagline">CERTIFIED BIODYNAMIC CRANIOSACRAL TRAININGS</p>

    <div class="plate plate--1"><div class="plate-face plate-face--name">DR. MARA<br>VELDEN</div></div>
    <div class="plate plate--2"><div class="plate-face plate-face--service">CRANIOSACRAL</div></div>
    <div class="plate plate--3"><div class="plate-face plate-face--service-lg">NUTRITION</div></div>
    <div class="plate plate--4"><div class="plate-face plate-face--phone">413 555-0148</div></div>

    <div class="bracket bracket--left bracket--r1"></div><div class="bracket bracket--right bracket--r1"></div>
    <div class="bracket bracket--left bracket--r2"></div><div class="bracket bracket--right bracket--r2"></div>
    <div class="bracket bracket--left bracket--r3"></div><div class="bracket bracket--right bracket--r3"></div>
    <div class="bracket bracket--left bracket--r4"></div><div class="bracket bracket--right bracket--r4"></div>
  </section>

  <!-- finished colourway -->
  <section class="sign sign--finish" aria-label="Sign layout, finished colours">
    <div class="header-band"></div>
    <div class="post post--outer-left"></div>
    <div class="post post--core-left"></div>
    <div class="post post--core-right"></div>
    <div class="post post--outer-right"></div>
    <div class="header-board"></div>
    <div class="header-frame"></div>
    <p class="practitioner">DR. MARA VELDEN, DC, BCST</p>
    <div class="ornament" role="img" aria-label="Small knotwork ornament"></div>
    <h2 class="school-name">LUMEN<br>HARBOR</h2>
    <div class="emblem" role="img" aria-label="Area for the school emblem artwork"></div>
    <div class="header-rule"></div>
    <p class="tagline">CERTIFIED BIODYNAMIC CRANIOSACRAL TRAININGS</p>

    <div class="plate plate--1"><div class="plate-face plate-face--name">DR. MARA<br>VELDEN</div></div>
    <div class="plate plate--2"><div class="plate-face plate-face--service">CRANIOSACRAL</div></div>
    <div class="plate plate--3"><div class="plate-face plate-face--service-lg">NUTRITION</div></div>
    <div class="plate plate--4"><div class="plate-face plate-face--phone">413 555-0148</div></div>

    <div class="bracket bracket--left bracket--r1"></div><div class="bracket bracket--right bracket--r1"></div>
    <div class="bracket bracket--left bracket--r2"></div><div class="bracket bracket--right bracket--r2"></div>
    <div class="bracket bracket--left bracket--r3"></div><div class="bracket bracket--right bracket--r3"></div>
    <div class="bracket bracket--left bracket--r4"></div><div class="bracket bracket--right bracket--r4"></div>
  </section>

</body>
</html>
```